I need a label design to go on our jars of honey. Our company is called Quillbrook Honey Co. The type of honey is called Marram Glade Honey. The jars are 1kg. Attached is the label size. Left hand side needs to have nutritional info... as attached. Middle section is our company name, honey type, 1kg & Whangamata, NZ. Right hand side needs to have info as per photo (raw honey etc). I would like to upload more pictures... but I’m unsure how to do this? Thanks, Noreen

Target Market(s)

Honey consumers... families

Industry/Entity Type

Food Production

Colors

Designer to choose colors to be used in the design.

Requirements
Must have
• Nutritional info as per upload
• Type of honey & company name as per upload
• 1kg
• Address
Nice to have
• Similar fonts to upload.
• Possibly background image... floral or beach... very faint though.

```html
<!DOCTYPE html>
<html lang="en">
<head>
<meta charset="utf-8">
<title>Quillbrook Honey Co. – Marram Glade Honey 1kg label</title>
<link href="https://fonts.googleapis.com/css2?family=Kalam:wght@300;400&family=Pathway+Gothic+One&family=Kaushan+Script&display=swap" rel="stylesheet">
<style>
  :root{
    --honey:#f59c34;
    --honey-soft:rgba(245,156,52,0);
    --ink:#262322;
    --paper:#eeebe9;
    --bloom-core:#f3cfa6;
    --bloom-mid:#f5e4d6;
    --bloom-edge:#f1e9e6;
  }
  *{margin:0;padding:0;box-sizing:border-box}
  html,body{width:1200px;height:481px;overflow:hidden;background:var(--paper)}
  .label{position:relative;width:1200px;height:481px;overflow:hidden;background:var(--paper);color:var(--ink);
    font-family:"Kalam",cursive;font-weight:300}
  .backdrop{position:absolute;inset:0;
    background:
      radial-gradient(ellipse 150px 90px at 740px 215px,var(--bloom-core) 0%,rgba(243,207,166,0) 100%),
      radial-gradient(ellipse 430px 230px at 620px 250px,var(--bloom-mid) 0%,var(--bloom-edge) 65%,var(--paper) 100%)}
  .drip-border{position:absolute;left:0;top:0;width:1200px;height:92px;z-index:3;
    background:linear-gradient(to bottom,var(--honey) 0,var(--honey) 24px,rgba(245,156,52,.55) 44px,var(--honey-soft) 92px)}

  /* nutrition panel */
  .nutrition{position:absolute;left:37px;top:88px;width:327px;height:255px;border:2px solid var(--honey);
    background:rgba(255,255,255,.9);font-size:15.5px;line-height:1}
  .nutrition .head{height:58px;border-bottom:2px solid var(--honey);padding:4px 0 0 19px}
  .nutrition .title{font-size:15.5px}
  .nutrition .head p{margin-top:1px;font-size:14.5px;line-height:17px}
  .nutrition .cols{height:54px;border-bottom:2px solid var(--honey);position:relative;font-size:14.5px}
  .nutrition .cols span{position:absolute;top:4px;line-height:14.5px}
  .c1{left:26px}.c2{left:118px}.c3{left:236px}
  .nutrition .rows{position:relative;padding-top:3px}
  .row{position:relative;height:17.8px}
  .row span{position:absolute;top:0}

  .storage{position:absolute;left:37px;width:327px;top:348px;text-align:center;font-size:14.5px;line-height:14.6px}
  .batch{position:absolute;left:97px;top:412px;width:207px;height:58px;border:2px solid var(--honey);
    background:rgba(255,255,255,.9);font-size:14.5px;line-height:14.6px;padding:5px 0 0 10px}
  .batch div{display:flex}.batch b{font-weight:300;width:88px}

  /* centre panel */
  .brand{position:absolute;left:0;width:1200px;text-align:center;font-weight:400}
  .brand-name{top:62px;font-family:"Pathway Gothic One",sans-serif;font-size:39px;line-height:43px;letter-spacing:.5px}
  .variety{top:190px;font-family:"Kaushan Script",cursive;font-size:44px;line-height:56px}
  .weight{top:346px;font-size:20px}
  .origin{top:407px;font-family:"Pathway Gothic One",sans-serif;font-size:24px;letter-spacing:.3px}

  /* story panel */
  .story{position:absolute;left:850px;width:265px;top:70px;text-align:center;font-size:14.5px;line-height:20.3px}
  .story p{margin-bottom:20.3px}
  .story p.lead{margin-bottom:40.6px}
</style>
</head>
<body>
<main class="label">
  <div class="backdrop" role="img" aria-label="Very faint photograph of a pale flower with a honey bee at its centre"></div>
  <div class="drip-border" role="img" aria-label="Orange honey drips running down from the top edge"></div>

  <section class="nutrition">
    <div class="head">
      <div class="title">NUTRITIONAL INFORMATION</div>
      <p>Serving per package: 100</p>
      <p>Serving size: 10g</p>
    </div>
    <div class="cols">
      <span class="c2">Average<br>Quantity<br>per Serving</span>
      <span class="c3">Average<br>Quantity<br>per 100g</span>
    </div>
    <div class="rows">
      <div class="row"><span class="c1">Energy</span><span class="c2">134kj</span><span class="c3">1340kj</span></div>
      <div class="row"><span class="c1">Protein</span><span class="c2">0.04g</span><span class="c3">0.4g</span></div>
      <div class="row"><span class="c1">Fat total</span><span class="c2">0g</span><span class="c3">0g</span></div>
      <div class="row"><span class="c1">-saturated</span><span class="c2">0g</span><span class="c3">0g</span></div>
      <div class="row"><span class="c1">Carbohydrate</span><span class="c2">7.9g</span><span class="c3">79.6g</span></div>
      <div class="row"><span class="c1">-Sugars</span><span class="c2">7.8g</span><span class="c3">78.1g</span></div>
      <div class="row"><span class="c1">Sodium</span><span class="c2">1.2mg</span><span class="c3">12mg</span></div>
    </div>
  </section>

  <p class="storage">Store upright in a cool, dry place.<br>No refrigeration needed.<br>Not recommended for infants below<br>the age of 12 months.</p>

  <div class="batch">
    <div><b>Best before</b>:</div>
    <div><b>RMP</b>:</div>
    <div><b>Batch No</b>:</div>
  </div>

  <h1 class="brand brand-name">QUILLBROOK<br>HONEY CO.</h1>
  <h2 class="brand variety">Marram Glade<br>Honey</h2>
  <p class="brand weight">1Kg</p>
  <p class="brand origin">WHANGAMATA N.Z.</p>

  <section class="story">
    <p class="lead">Sourced from the beautiful<br>Coromandel Peninsula.</p>
    <p>Our honey comes to you raw &amp;<br>unpasteurised, ensuring it retains<br>all natural goodness!</p>
    <p>Arohanui,<br>Corwin, Noreen &amp; boys</p>
    <p>'Quillbrook'- all thanks to God for His<br>incredible creation!</p>
    <p>www.quillbrookhoney.co.nz<br>47 Tidewell St<br>Whangamata<br>New Zealand</p>
  </section>
</main>
</body>
</html>
```